Instructions for nurses on how to give a report on each shift

I have a 2-page reference sheet that needs to be updated to look more aesthetically pleasing.

Target Market(s)

Healthcare, nurses

Industry/Entity Type

Healthcare

Font styles to use
Sans Serif

Requirements
Must have
• Please make sure it is easy to read, the content is well organized and has a flow to it. Please also pick colors that would coordinate with our website www.brivolen.org (so mainly navy and white or off-white with accent colors.) Please make sure to add accent colors to break up the content. The MORVY name and title at the top should remain on the page but I'm not married to the star or logo style. You can do what you think looks best there. Way at the bottom in fine print, I would like for you to add BRIVOLEN © 2019 All rights reserved.

```html
<!DOCTYPE html>
<html lang="en">
<head>
<meta charset="utf-8">
<title>MORVY Shift Report Sheet</title>
<link href="https://fonts.googleapis.com/css2?family=Roboto:wght@300;400;500;700&display=swap" rel="stylesheet">
<style>
:root{
  --navy:#1d3a5f;
  --navy-deep:#17304f;
  --sky:#cfe2f3;
  --panel:#d6e6f5;
  --accent:#e8e84a;
  --ink:#2b2b2b;
  --line:#555;
  --muted:#6b7380;
  --paper:#ffffff;
  --card:#eef1f4;
  --floral:#e3ecf5;
}
*{box-sizing:border-box;margin:0;padding:0}
html,body{width:900px;height:1200px;overflow:hidden;background:var(--paper)}
body{font-family:"Roboto",Arial,sans-serif;color:var(--ink);position:relative}
.sheet{position:absolute;inset:0;overflow:hidden}
.floral{position:absolute;border-radius:50%;background:radial-gradient(circle,var(--floral) 0%,rgba(227,236,245,0) 70%)}
.floral.top-right{right:-60px;top:-80px;width:520px;height:300px}
.floral.bottom-left{left:-120px;bottom:-120px;width:420px;height:320px}
.floral.bottom-right{right:-100px;bottom:-120px;width:380px;height:320px}

.brand{position:absolute;left:38px;top:28px;display:flex;align-items:flex-start;gap:10px}
.brand-dot{width:26px;height:26px;border-radius:50%;background:var(--navy);margin-top:4px}
.brand-name{font-weight:700;font-size:30px;color:var(--navy);letter-spacing:1px;line-height:1}
.brand-tagline{font-size:8.5px;color:var(--navy);line-height:1.25;margin-top:4px;text-transform:uppercase;letter-spacing:.3px}

.leader-card{position:absolute;left:36px;top:88px;width:190px;height:195px;background:var(--card);transform:rotate(-2deg);box-shadow:3px 4px 6px rgba(0,0,0,.18)}
.leader-avatar{position:absolute;left:34px;top:22px;width:124px;height:124px;border-radius:50%;background:linear-gradient(180deg,#a9cfe8,#7fb4da)}
.leader-label{position:absolute;left:0;right:0;bottom:14px;text-align:center;font-size:19px;letter-spacing:1px;color:var(--ink)}

.fields{position:absolute;left:248px;top:140px;width:610px}
.field{display:flex;align-items:flex-end;height:38px;font-size:21px;color:var(--ink)}
.field span{flex:1;border-bottom:1.5px solid var(--line);margin-left:6px;height:20px}

.section{position:absolute;left:0;width:900px}
.step-number{position:absolute;left:40px;top:0;width:72px;height:72px;border-radius:50%;border:6px solid var(--navy);background:var(--paper);display:flex;align-items:center;justify-content:center;font-size:44px;font-weight:300;color:var(--navy);z-index:2}
.topics{position:absolute;left:40px;top:36px;width:122px;background:var(--panel);padding:48px 0 18px 10px;list-style:none}
.topics.compact{padding-top:40px;padding-bottom:10px}
.topics li{font-size:15px;line-height:26px;color:var(--ink);padding-left:14px;position:relative}
.topics li::before{content:"";position:absolute;left:0;top:11px;width:5px;height:5px;border-radius:50%;background:var(--ink)}
.question{position:absolute;left:176px;top:10px;background:var(--accent);border-radius:14px;padding:3px 10px;font-size:17px;color:var(--navy)}
.answer{position:absolute;left:176px;width:614px;height:50px;display:flex;align-items:center;font-size:16px}
.answer.no{background:var(--navy-deep);color:#fff}
.answer.yes{background:var(--sky);color:var(--ink)}
.answer-tag{width:70px;text-align:center;font-size:34px;font-weight:300;margin-right:10px}
.answer.no .answer-tag{border:2px solid #fff;border-radius:6px;margin-left:10px;width:54px;height:40px;line-height:38px;font-size:30px}
.answer.yes .answer-tag{color:var(--navy)}
.check{position:absolute;left:800px;width:46px;height:46px;border-radius:50%;border:2px solid var(--sky);background:var(--paper)}
.entries{position:absolute;left:176px;width:620px;display:flex;justify-content:space-between}
.entry{width:190px;font-size:16px}
.entry .row{display:flex;align-items:flex-end}
.entry .row span{flex:1;border-bottom:1.2px solid var(--line);margin-left:4px;height:14px}
.entry .under{border-bottom:1.2px solid var(--line);margin-top:26px;height:1px}

.fine-print{position:absolute;left:0;right:0;bottom:22px;text-align:center;font-size:10px;color:var(--muted);letter-spacing:.3px}
</style>
</head>
<body>
<main class="sheet">
  <div class="floral top-right" role="img" aria-label="Faint hibiscus flower decoration"></div>
  <div class="floral bottom-left" role="img" aria-label="Faint hibiscus flower decoration"></div>
  <div class="floral bottom-right" role="img" aria-label="Faint hibiscus flower decoration"></div>

  <header class="brand">
    <div class="brand-dot"></div>
    <div>
      <div class="brand-name">MORVY</div>
      <div class="brand-tagline">Making Outcomes Reliable Through Vigilant Care<br>and Yielding Excellence</div>
    </div>
  </header>

  <div class="leader-card">
    <div class="leader-avatar" role="img" aria-label="Illustration of a nurse leader"></div>
    <div class="leader-label">LEADER</div>
  </div>

  <div class="fields">
    <div class="field">Name:<span></span></div>
    <div class="field">Title:<span></span></div>
    <div class="field">Assignment:<span></span></div>
  </div>

  <section class="section" style="top:298px">
    <div class="step-number">1</div>
    <ul class="topics" style="height:220px"><li>Admissions</li><li>Discharges</li><li>Transfers</li><li>Appointments</li></ul>
    <div class="question">Any change in resident status?</div>
    <div class="answer no" style="top:57px"><span class="answer-tag">NO</span>“I do not have any actual or expected changes in resident status”</div>
    <div class="check" style="top:59px"></div>
    <div class="answer yes" style="top:132px"><span class="answer-tag">YES</span>“My residents with changes in their status are…”</div>
    <div class="check" style="top:134px"></div>
    <div class="entries" style="top:200px">
      <div class="entry"><div class="row">1)<span></span></div><div class="under"></div></div>
      <div class="entry"><div class="row">2)<span></span></div><div class="under"></div></div>
      <div class="entry"><div class="row">3)<span></span></div><div class="under"></div></div>
    </div>
  </section>

  <section class="section" style="top:578px">
    <div class="step-number">2</div>
    <ul class="topics compact" style="height:232px"><li>Pain</li><li>Skin</li><li>Ambulation</li><li>Safety</li><li>Behavior</li><li>Appetite</li><li>Elimination</li></ul>
    <div class="question">Any concerning changes in resident’s condition?</div>
    <div class="answer no" style="top:57px"><span class="answer-tag">NO</span>“I have no residents with concerning changes in their condition”</div>
    <div class="check" style="top:59px"></div>
    <div class="answer yes" style="top:132px"><span class="answer-tag">YES</span>“My residents with concerning changes in their condition include…”</div>
    <div class="check" style="top:134px"></div>
    <div class="entries" style="top:200px">
      <div class="entry"><div class="row">1)<span></span></div><div class="under"></div></div>
      <div class="entry"><div class="row">2)<span></span></div><div class="under"></div></div>
      <div class="entry"><div class="row">3)<span></span></div><div class="under"></div></div>
    </div>
  </section>

  <section class="section" style="top:860px">
    <div class="step-number">3</div>
    <ul class="topics" style="height:220px"><li>Falls</li><li>Decline<br>in condition</li><li>IV/ABT<br>therapy</li><li>Hospice</li></ul>
    <div class="question">Any residents requiring extraordinary monitoring?</div>
    <div class="answer no" style="top:57px"><span class="answer-tag">NO</span>“I have no residents requiring extraordinary monitoring”</div>
    <div class="check" style="top:59px"></div>
    <div class="answer yes" style="top:132px"><span class="answer-tag">YES</span>“My residents that require extraordinary monitoring are…”</div>
    <div class="check" style="top:134px"></div>
    <div class="entries" style="top:200px">
      <div class="entry"><div class="row">1)<span></span></div><div class="under"></div></div>
      <div class="entry"><div class="row">2)<span></span></div><div class="under"></div></div>
      <div class="entry"><div class="row">3)<span></span></div><div class="under"></div></div>
    </div>
  </section>

  <footer class="fine-print">BRIVOLEN © 2019 All rights reserved.</footer>
</main>
</body>
</html>
```